Illustrate a statistic and its significance

Please create a graphical representation of the success rate of the Vail Procedure for our website. The Vail Procedure has a success rate of 80%. This means the procedure is successful for 8 out of every 10 people. An 80% success rate by itself is great. However, it's even more impressive when you consider that the only people we perform this procedure on are patients who have exhausted conventional treatment options for migraines and headaches. I would really like to emphasize both the success rate and the type of patients we are successful in treating with this procedure.
For example, you could create an illustration of outlines of 10 people with 8 of them shaded in, which would represent an 80% success rate. Then, underneath this image, you could add a bullet list of the types of treatments patients (such as the 10 figures in the image) have tried before coming to us/having this procedure, which include the following:
Prescription medications
Trigger point injections
Nerve blocks
Migraine surgery
Dermil
Chiropractic care
Physical therapy
Biofeedback
Massage
Acupuncture
Or maybe there is another/better way to represent this statistic graphically? I'm just looking for an effective illustration of this important statistic and its significance.
Our brand colors are red (#fd444a) and blue (#214170)
Thank you!
People who suffer from chronic migraines and headaches
Healthcare/Medical
- Athiti

```html
<!DOCTYPE html>
<html lang="en">
<head>
<meta charset="utf-8">
<title>Vail Procedure Success Rate</title>
<link href="https://fonts.googleapis.com/css2?family=Poppins:wght@400;500;700;800&display=swap" rel="stylesheet">
<style>
  :root {
    --brand-red: #fd444a;
    --brand-blue: #214170;
    --page-bg: #f1f1f3;
    --rule-grey: #d3d3d5;
    --white: #ffffff;
  }
  * { margin: 0; padding: 0; box-sizing: border-box; }
  html, body { width: 1200px; height: 1200px; overflow: hidden; }
  body {
    background: var(--page-bg);
    font-family: 'Poppins', sans-serif;
    color: var(--brand-blue);
    position: relative;
  }
  .headline {
    position: absolute; left: 104px; top: 48px;
    font-weight: 800; font-size: 65px; line-height: 71px;
    letter-spacing: -0.5px; text-transform: uppercase;
  }
  .headline .line-blue { color: var(--brand-blue); display: block; }
  .headline .line-red { color: var(--brand-red); display: block; }
  .headline-rule {
    position: absolute; left: 107px; top: 202px;
    width: 192px; height: 7px; background: var(--brand-blue);
  }
  .people-grid {
    position: absolute; left: 107px; top: 280px;
    display: grid; grid-template-columns: repeat(5, 73px);
    column-gap: 19px; row-gap: 10px;
  }
  .person {
    width: 73px; height: 180px; border-radius: 36px 36px 8px 8px;
  }
  .person.success { background: var(--brand-red); }
  .person.other { background: var(--brand-blue); }
  .rate-ring { position: absolute; left: 708px; top: 281px; width: 368px; height: 368px; }
  .rate-label {
    position: absolute; left: 768px; top: 390px; width: 248px;
    text-align: center;
  }
  .rate-label .figure {
    display: block; color: var(--brand-red);
    font-weight: 800; font-size: 84px; line-height: 76px;
  }
  .rate-label .caption {
    display: block; font-weight: 500; font-size: 38px; line-height: 34px;
  }
  .history {
    position: absolute; left: 107px; top: 725px; height: 387px;
    border-left: 13px solid var(--rule-grey); padding-left: 35px;
  }
  .history h2 {
    font-weight: 500; font-size: 40px; line-height: 53px; margin-top: -8px;
  }
  .history ul { list-style: none; margin-top: 20px; }
  .history li { font-size: 23px; line-height: 39px; }
  .history .sep { color: var(--brand-red); margin: 0 8px; }
  .candidate-note {
    position: absolute; left: 679px; top: 705px; width: 425px; height: 435px;
    border: 2px dashed var(--brand-blue);
  }
  .headache-icon {
    position: absolute; left: 47px; top: 15px; width: 158px; height: 140px;
    background: var(--brand-blue); border-radius: 70px 70px 6px 6px;
  }
  .candidate-note p {
    position: absolute; left: 47px; top: 170px; width: 370px;
    font-weight: 700; font-size: 25.5px; line-height: 40px;
  }
</style>
</head>
<body>
  <h1 class="headline">
    <span class="line-blue">The Vail Procedure has</span>
    <span class="line-red">a success rate of 80%</span>
  </h1>
  <div class="headline-rule"></div>

  <div class="people-grid">
    <div class="person success" role="img" aria-label="Person figure, successful outcome"></div>
    <div class="person success" role="img" aria-label="Person figure, successful outcome"></div>
    <div class="person success" role="img" aria-label="Person figure, successful outcome"></div>
    <div class="person success" role="img" aria-label="Person figure, successful outcome"></div>
    <div class="person success" role="img" aria-label="Person figure, successful outcome"></div>
    <div class="person success" role="img" aria-label="Person figure, successful outcome"></div>
    <div class="person success" role="img" aria-label="Person figure, successful outcome"></div>
    <div class="person success" role="img" aria-label="Person figure, successful outcome"></div>
    <div class="person other" role="img" aria-label="Person figure, other outcome"></div>
    <div class="person other" role="img" aria-label="Person figure, other outcome"></div>
  </div>

  <svg class="rate-ring" viewBox="0 0 368 368" aria-label="Donut chart showing 80% success">
    <circle cx="184" cy="184" r="124" fill="var(--white)"/>
    <circle cx="184" cy="184" r="154" fill="none" stroke="var(--brand-red)" stroke-width="60"/>
    <circle cx="184" cy="184" r="154" fill="none" stroke="var(--brand-blue)" stroke-width="60"
      stroke-dasharray="193.5 1000" transform="rotate(-90 184 184)"/>
  </svg>
  <div class="rate-label">
    <span class="figure">80%</span>
    <span class="caption">SUCCESS<br>RATE</span>
  </div>

  <section class="history">
    <h2>Treatments patients<br>have tried before<br>coming to us</h2>
    <ul>
      <li>Prescription medications</li>
      <li>Trigger point injections</li>
      <li>Nerve blocks<span class="sep">|</span>Migraine surgery</li>
      <li>Dermil<span class="sep">|</span>Chiropractic care</li>
      <li>Physical therapy<span class="sep">|</span>Biofeedback</li>
      <li>Massage<span class="sep">|</span>Acupuncture</li>
    </ul>
  </section>

  <aside class="candidate-note">
    <div class="headache-icon" role="img" aria-label="Icon of a person holding their head in pain"></div>
    <p>The procedure is only performed on patients who have exhausted conventional treatment options for migraines and headaches.</p>
  </aside>
</body>
</html>
```